Business Card Design Project

Basic business card with minimal details. I just need company name, email & web address, telephone and my name.
I would like the back of the card to be grey with my logo & company name centred.

Target Market(s)

Architects
Builders
Property Developers

Industry/Entity Type

Business

Font styles to use
Sans Serif

Colors

Designer to choose colors to be used in the design.

Requirements
Must have
• Framewise Build
Marcus Helby - Director
M: 0427 593184
E: marcus@framewisebuild.com.au
W: www.framewisebuild.com.au
Should not have
• No other images or pictures

```html
<!DOCTYPE html>
<html lang="en">
<head>
<meta charset="utf-8">
<title>Framewise Build – Business Cards</title>
<link href="https://fonts.googleapis.com/css2?family=Lato:wght@400&display=swap" rel="stylesheet">
<style>
  :root {
    --backdrop: #e8e5e1;
    --paper: #ffffff;
    --ink-slate: #4b5866;
    --brand-red: #b8213f;
    --panel-black: #050505;
    --contact-white: #f2f2f2;
  }
  * { margin: 0; padding: 0; box-sizing: border-box; }
  html, body {
    width: 1200px;
    height: 800px;
    overflow: hidden;
    background: var(--backdrop);
    font-family: "Lato", Arial, sans-serif;
  }
  .stage {
    position: relative;
    width: 1200px;
    height: 800px;
    display: flex;
    align-items: center;
    justify-content: center;
    gap: 60px;
  }
  .card {
    position: relative;
    width: 500px;
    height: 286px;
    background: var(--paper);
    overflow: hidden;
    box-shadow: 0 6px 18px rgba(0,0,0,0.12);
  }

  /* brand lockup */
  .brand {
    position: absolute;
    left: 0;
    right: 0;
    display: flex;
    flex-direction: column;
    align-items: center;
  }
  .brand-mark {
    width: 38px;
    height: 38px;
    background: var(--brand-red);
  }
  .brand-name {
    margin-top: 16px;
    font-size: 22px;
    font-weight: 400;
    letter-spacing: 0.14em;
    text-transform: uppercase;
    color: var(--ink-slate);
    white-space: nowrap;
  }
  .card-front .brand { top: 96px; }

  /* contact side */
  .card-back .brand { top: 30px; }
  .card-back .brand-mark { width: 30px; height: 30px; }
  .card-back .brand-name { margin-top: 12px; font-size: 17px; }

  .accent-band {
    position: absolute;
    left: 0;
    right: 0;
    top: 140px;
    height: 9px;
    background: var(--brand-red);
  }
  .info-panel {
    position: absolute;
    left: 0;
    right: 0;
    top: 149px;
    bottom: 0;
    background: var(--panel-black);
  }
  .holder-name {
    position: absolute;
    left: 34px;
    bottom: 34px;
    font-size: 27px;
    color: var(--brand-red);
    letter-spacing: 0.01em;
  }
  .contact-list {
    position: absolute;
    right: 28px;
    top: 26px;
    list-style: none;
  }
  .contact-item {
    display: flex;
    align-items: center;
    gap: 9px;
    font-size: 12.5px;
    line-height: 22px;
    color: var(--contact-white);
  }
  .contact-icon {
    width: 11px;
    height: 11px;
    flex: none;
    fill: var(--brand-red);
  }
</style>
</head>
<body>
<main class="stage">

  <section class="card card-front" aria-label="Card front">
    <div class="brand">
      <span class="brand-mark" aria-hidden="true"></span>
      <span class="brand-name">Framewise Build</span>
    </div>
  </section>

  <section class="card card-back" aria-label="Card contact side">
    <div class="brand">
      <span class="brand-mark" aria-hidden="true"></span>
      <span class="brand-name">Framewise Build</span>
    </div>
    <div class="accent-band"></div>
    <div class="info-panel">
      <ul class="contact-list">
        <li class="contact-item">
          <svg class="contact-icon" viewBox="0 0 12 12" aria-hidden="true">
            <path d="M2.4 0.6 L4.2 0.6 L5 3.2 L3.8 4.2 C4.5 5.7 6.3 7.5 7.8 8.2 L8.8 7 L11.4 7.8 L11.4 9.6 C11.4 10.6 10.6 11.4 9.6 11.4 C4.6 11.1 0.9 7.4 0.6 2.4 C0.6 1.4 1.4 0.6 2.4 0.6 Z"/>
          </svg>
          <span>0427 593184</span>
        </li>
        <li class="contact-item">
          <svg class="contact-icon" viewBox="0 0 12 12" aria-hidden="true">
            <path d="M0.5 2 H11.5 V10 H0.5 Z M1.3 2.8 L6 6.6 L10.7 2.8" fill="var(--brand-red)"/>
            <path d="M1.2 3 L6 6.8 L10.8 3" fill="none" stroke="#050505" stroke-width="1"/>
          </svg>
          <span>marcus@framewisebuild.com.au</span>
        </li>
        <li class="contact-item">
          <svg class="contact-icon" viewBox="0 0 12 12" aria-hidden="true">
            <circle cx="6" cy="6" r="5" fill="none" stroke="var(--brand-red)" stroke-width="1.3"/>
            <path d="M1 6 H11 M6 1 C3.8 3.5 3.8 8.5 6 11 M6 1 C8.2 3.5 8.2 8.5 6 11" fill="none" stroke="var(--brand-red)" stroke-width="1"/>
          </svg>
          <span>www.framewisebuild.com.au</span>
        </li>
      </ul>
      <p class="holder-name">Marcus Helby</p>
    </div>
  </section>

</main>
</body>
</html>
```